Garlic Farm for Farm Sales/Restaurant sales

Need a professional, but appealing to agriculture world. We are selling 27 kinds of Organic Garlic from a farm in Simla,CO. I have uploaded logo and business information-we are going to need a template, because I will need to use it for four separate people.
-We are trying to appeal to Farm to table restaurants
-As well as growers/farmers

Target Market(s)

Agriculture Sales/Restaurants-Organic

Industry/Entity Type

Agriculture

Contact Information for Business Card

Want it to look more unique then your average orbel mart card- I want it to look amazing

Font styles to use
Sans Serif

Colors
0455a3
ec1f27
fbed22
ffffff

Requirements
Must have
• Just be creative
Nice to have
• Colorful
Should not have
• plain

```html
<!DOCTYPE html>
<html lang="en">
<head>
<meta charset="utf-8">
<title>Summit Ridge Garlic – Business Card</title>
<link href="https://fonts.googleapis.com/css2?family=Roboto:wght@400;700&display=swap" rel="stylesheet">
<style>
  :root {
    --bg: #d9d9dc;
    --card: #ffffff;
    --plum: #3d2f5b;
    --navy: #1c2f66;
    --red: #c9222b;
    --yellow: #fbe122;
    --white: #ffffff;
    --text-font: "Roboto", Arial, sans-serif;
  }
  * { box-sizing: border-box; margin: 0; padding: 0; }
  html, body { width: 1200px; height: 852px; overflow: hidden; }
  body {
    background: var(--bg);
    font-family: var(--text-font);
    display: flex;
    align-items: center;
    justify-content: center;
    gap: 40px;
  }
  .card {
    position: relative;
    width: 540px;
    height: 309px;
    background: var(--card);
    border-radius: 18px;
    overflow: hidden;
    box-shadow: 0 6px 18px rgba(0,0,0,.18);
  }
  .brand {
    position: absolute;
    display: flex;
    align-items: center;
    gap: 12px;
    color: var(--navy);
    font-weight: 700;
    line-height: 1.1;
  }
  .brand-dot {
    border-radius: 50%;
    background: var(--red);
    flex: none;
  }
  .card-front .brand { left: 50%; top: 50%; transform: translate(-50%, -50%); font-size: 34px; white-space: nowrap; }
  .card-front .brand-dot { width: 56px; height: 56px; }

  .card-back .swoosh { position: absolute; inset: 0; width: 100%; height: 100%; }
  .card-back .brand { right: 34px; top: 70px; font-size: 24px; gap: 10px; }
  .card-back .brand-dot { width: 44px; height: 44px; }
  .brand-name { display: block; }
  .socials { position: absolute; right: 40px; top: 160px; display: flex; gap: 10px; }
  .socials span { width: 16px; height: 16px; border-radius: 50%; background: var(--navy); }

  .person { position: absolute; left: 48px; top: 88px; }
  .person-name { color: var(--white); font-size: 22px; font-weight: 700; }
  .person-role { color: var(--yellow); font-size: 14px; font-weight: 700; margin-top: 4px; }

  .contacts { position: absolute; left: 48px; bottom: 30px; list-style: none; }
  .contacts li {
    display: flex; align-items: center; gap: 8px;
    color: var(--white); font-size: 12.5px; line-height: 20px;
  }
  .contacts svg { width: 12px; height: 12px; flex: none; }
</style>
</head>
<body>

<section class="card card-front" aria-label="Card front">
  <div class="brand"><span class="brand-dot"></span>Summit Ridge Garlic</div>
</section>

<section class="card card-back" aria-label="Card back">
  <svg class="swoosh" viewBox="0 0 540 309" preserveAspectRatio="none" aria-hidden="true">
    <path d="M0 0 H300 C262 120 300 232 540 262 V309 H0 Z" fill="var(--yellow)"/>
    <path d="M0 0 H300 C262 120 300 225 540 250 V309 H0 Z" fill="var(--white)"/>
    <path d="M0 0 H292 C252 125 295 238 540 270 V309 H0 Z" fill="var(--plum)"/>
    <path d="M0 0 H300 C262 120 300 232 540 262 V268 C292 240 254 125 292 0 Z" fill="var(--yellow)"/>
    <path d="M312 0 C278 112 306 214 540 240" fill="none" stroke="var(--red)" stroke-width="5"/>
    <path d="M322 0 C292 104 318 206 540 230" fill="none" stroke="var(--plum)" stroke-width="2"/>
  </svg>

  <div class="person">
    <p class="person-name">Dana Holt</p>
    <p class="person-role">President</p>
  </div>

  <ul class="contacts">
    <li><svg viewBox="0 0 12 12"><path d="M2 1 L4.5 1 L5.2 3.6 L3.8 4.6 C4.5 6 5.9 7.4 7.4 8.2 L8.4 6.8 L11 7.5 V10 C11 10.6 10.6 11 10 11 C5.2 11 1 6.8 1 2 C1 1.4 1.4 1 2 1 Z" fill="var(--yellow)"/></svg>555-010-4827</li>
    <li><svg viewBox="0 0 12 12"><rect x="0.5" y="2" width="11" height="8" fill="var(--yellow)"/><path d="M0.5 2 L6 6.5 L11.5 2" fill="none" stroke="var(--plum)" stroke-width="1"/></svg>Dana@SRGarlic.com</li>
    <li><svg viewBox="0 0 12 12"><circle cx="6" cy="6" r="5" fill="none" stroke="var(--yellow)" stroke-width="1.2"/><ellipse cx="6" cy="6" rx="2.2" ry="5" fill="none" stroke="var(--yellow)" stroke-width="1"/><path d="M1 6 H11" stroke="var(--yellow)" stroke-width="1"/></svg>www.SRGarlic.com</li>
    <li><svg viewBox="0 0 12 12"><path d="M6 11.5 C6 11.5 1.8 7 1.8 4.6 A4.2 4.2 0 0 1 10.2 4.6 C10.2 7 6 11.5 6 11.5 Z" fill="var(--yellow)"/><circle cx="6" cy="4.6" r="1.5" fill="var(--plum)"/></svg>P.O. Box 12 Elkton, CO 80000</li>
  </ul>

  <div class="brand"><span class="brand-dot"></span><span class="brand-name">Summit Ridge<br>Garlic</span></div>
  <div class="socials" aria-hidden="true"><span></span><span></span><span></span><span></span></div>
</section>

</body>
</html>
```